Rovquill

Hi everyone!

Looks like our project is more sophisticated than we expected. So good news - we increased the budget! and one of you will sure get the prize - no money back for us!

We are a young Russian company that specializes in in-taxi entertainment. We believe that our key strength is great attention to user experience. We've devoted much effort to improve ergonomics of our devices - tablet PCs that we install in the taxis. And yes, we enjoy to simplify things!

Now we need the most basic things - a logo and some staff for client meetings (primarily advertisers and ad agencies).

As for logo - we already have one engraved on the prototypes of our device (see attached file). This is one of the ideas (still far from perfect) - what we appreciate in it is minimalistic yet stylish approach.

As for "take it to the meeting stuff" we want to start with name card, pen and notepad (A4) that we will leave in clients's office, also as a reminder. Shall your have more smart ideas - always welcome!

As for logo and name cards - we would like to make an image of serious but modern company. Our design should communicate creativity and reliability. We believe that "to understand is to simplify" - minimalistic design is the most difficult one. Its better to work hard on fonts and arrangement, than put 10 variegated images.

SO THE TASK IS TO DESIGN:
- a logo
- a name card
- a note pad (great example in attachment)
- a pen

Shall you have more questions - please ask in comments.

We look forward to meeting like-minded fellows here!

Target Market(s)

Out target are:

- advertiser
- advertising agencies
- taxi passenger

Industry/Entity Type

It Company

Requirements
Must have
• font should be chosen very carefully
Nice to have
• classic minimalistic plain text only but very stylish name card is a dream of one of our co-founders:)
Should not have
• we do not want to have taxi-like colors and chess-boards. We are closer to "innovation", "entertainment", and "user experience", rather than "taxi".

```html
<!DOCTYPE html>
<html lang="en">
<head>
<meta charset="utf-8">
<title>Rovquill stationery</title>
<link rel="stylesheet" href="https://fonts.googleapis.com/css2?family=Tinos&family=Open+Sans:wght@700&display=swap">
<style>
  :root {
    --ink: #24272b;
    --brand-blue: #2f7fe0;
    --band-blue: #3a72c4;
    --band-dark: #24364f;
    --frame: #2a2c2e;
    --grid-fine: #dfe3e6;
    --grid-major: #c7ccd0;
    --footer-grey: #cfd4d4;
    --paper: #ffffff;
    --divider: #d6d8da;
    --pen-light: #d4d6d8;
    --pen-dark: #6e7276;
  }
  html, body { margin: 0; padding: 0; overflow: hidden; }
  body {
    width: 1200px; height: 800px; position: relative;
    background: var(--paper);
    font-family: "Tinos", "Times New Roman", serif;
    color: var(--ink);
  }

  /* Notepad */
  .notepad {
    position: absolute; left: 12px; top: 32px; width: 514px; height: 728px;
    border: 4px solid var(--frame); background: var(--paper);
  }
  .notepad__grid {
    position: absolute; left: 4px; top: 4px; right: 4px; height: 652px;
    background-image:
      linear-gradient(to right, var(--grid-major) 2px, transparent 2px),
      linear-gradient(to bottom, var(--grid-major) 2px, transparent 2px),
      linear-gradient(to right, var(--grid-fine) 1px, transparent 1px),
      linear-gradient(to bottom, var(--grid-fine) 1px, transparent 1px);
    background-size: 85px 85px, 85px 85px, 8.5px 8.5px, 8.5px 8.5px;
    border-bottom: 4px solid var(--frame);
  }
  .notepad__footer {
    position: absolute; left: 0; right: 0; bottom: 0; height: 64px;
    background: var(--footer-grey);
  }
  .notepad__url { position: absolute; left: 10px; bottom: 8px; font-size: 14px; }
  .notepad__mark { position: absolute; right: 10px; bottom: 6px; text-align: center; }
  .notepad__mark .mark-circle { width: 36px; height: 36px; margin: 0 auto 1px; border-width: 2px; }
  .notepad__mark .wordmark { font-size: 18px; }

  /* Shared mark */
  .mark-circle { border: 3px solid var(--brand-blue); border-radius: 50%; box-sizing: border-box; }
  .wordmark { color: var(--ink); letter-spacing: 0.01em; line-height: 1; }

  /* Business card */
  .business-card {
    position: absolute; left: 553px; top: 32px; width: 625px; height: 358px;
    border: 1px solid #9aa0a4; background: var(--paper); overflow: hidden;
  }
  .business-card__brand {
    position: absolute; left: 53px; top: 121px; width: 212px; text-align: center;
  }
  .business-card__brand .mark-circle { width: 80px; height: 80px; margin: 0 auto 10px; }
  .business-card__brand .wordmark { font-size: 38px; }
  .business-card__divider {
    position: absolute; left: 301px; top: 68px; width: 1px; height: 240px; background: var(--divider);
  }
  .business-card__details {
    position: absolute; left: 330px; top: 67px; font-size: 19px; line-height: 22.5px;
  }
  .business-card__name {
    font-family: "Open Sans", Arial, sans-serif; font-weight: 700; font-size: 22px;
    letter-spacing: 0.03em; margin: 0; line-height: 26px;
  }
  .business-card__details p { margin: 0; }
  .business-card__details .business-card__address { margin-top: 11px; }
  .contact-list { margin-top: 13px; display: grid; grid-template-columns: 62px 22px auto; }
  .business-card__band {
    position: absolute; left: 0; right: 0; bottom: 0; height: 38px;
    background: linear-gradient(to bottom, var(--band-blue), var(--band-dark));
  }

  /* Logo display and pen */
  .logo-display { position: absolute; left: 577px; top: 482px; width: 316px; text-align: center; }
  .logo-display .mark-circle { width: 134px; height: 134px; margin: 0 auto 4px; border-width: 5px; }
  .logo-display .wordmark { font-size: 56px; }
  .pen-placeholder {
    position: absolute; left: 918px; top: 425px; width: 236px; height: 245px;
    background: linear-gradient(135deg, var(--pen-light), var(--pen-dark));
  }
</style>
</head>
<body>
  <section class="notepad" aria-label="A4 notepad">
    <div class="notepad__grid"></div>
    <div class="notepad__footer">
      <span class="notepad__url">www.rovquill.com.ru</span>
      <div class="notepad__mark">
        <div class="mark-circle"></div>
        <div class="wordmark">ROVQUILL</div>
      </div>
    </div>
  </section>

  <section class="business-card" aria-label="Name card">
    <div class="business-card__brand">
      <div class="mark-circle"></div>
      <div class="wordmark">ROVQUILL</div>
    </div>
    <div class="business-card__divider"></div>
    <div class="business-card__details">
      <h1 class="business-card__name">MAREK DOLL</h1>
      <p>Sales &amp; Marketing Director</p>
      <p>Mobile: 555-014-2270</p>
      <p class="business-card__address">Elsewhere on the map</p>
      <p>Global, PO Box 654321</p>
      <div class="contact-list">
        <span>Tel</span><span>:</span><span>55501234</span>
        <span>Fax</span><span>:</span><span>55509876</span>
        <span>E-mail</span><span>:</span><span>marek@rovquill.com.ru</span>
        <span>URL</span><span>:</span><span>www.rovquill.com.ru</span>
      </div>
    </div>
    <div class="business-card__band"></div>
  </section>

  <div class="logo-display">
    <div class="mark-circle"></div>
    <div class="wordmark">ROVQUILL</div>
  </div>

  <div class="pen-placeholder" role="img" aria-label="Illustration of the branded metallic ballpoint pen"></div>
</body>
</html>
```